Dental Trade Show Brochure

We need a brochure that is created for dental professionals that will explain how our Compliance Management Platform can help them to simplify, centralize and automate their compliance and other documentation requirements for their practices.

would like the content to be refreshed for dental practices. “EHS” should go away, as healthcare has many compliance requirements, not just health and safety. You are the experts. I am looking for your creative genius to help guide me to the right brochure that has text, imagery and design that will speak to my audience.
Updates

Target Market(s)

Dental Industry

Industry/Entity Type

Dental

Requirements
Must have
• would like the content to be refreshed for dental practices. “EHS” should go away, as healthcare has many compliance requirements, not just health and safety. You are the experts. I am looking for your creative genius to help guide me to the right brochure that has text, imagery and design that will speak to my audience.
Nice to have
• We prefer 1 front/back page over bi or tri fold
Should not have
• Other Industry graphics, design, content.

```html
<!DOCTYPE html>
<html lang="en">
<head>
<meta charset="utf-8">
<title>Verixa – Compliance for Dental Practices</title>
<link href="https://fonts.googleapis.com/css2?family=Fira+Sans:wght@600;700&family=Montserrat:wght@400;500&display=swap" rel="stylesheet">
<style>
  :root{
    --navy:#262a7a;
    --blue:#3548b0;
    --paper:#ffffff;
    --paper-tint:#f4f4fa;
    --band-grey:#e9e9f1;
    --ink:#1e1e2a;
    --white:#ffffff;
  }
  *{margin:0;padding:0;box-sizing:border-box}
  html,body{width:1200px;height:849px;overflow:hidden;background:var(--paper)}
  .brochure{position:relative;width:1200px;height:849px;overflow:hidden;font-family:"Montserrat",sans-serif;color:var(--ink)}
  .shapes{position:absolute;inset:0;width:1200px;height:849px}
  .abs{position:absolute}
  .body-copy{font-size:10.4px;line-height:17.7px;font-weight:400;letter-spacing:-.05px}
  .justify{text-align:justify}
  .heading{font-family:"Fira Sans",sans-serif;font-weight:700;color:var(--navy);letter-spacing:.1px}
  .main-title{left:32px;top:186px;font-size:41px;line-height:46px}
  .section-title{font-size:18.5px;line-height:24px}
  .feature-list{list-style:none}
  .feature-list li{position:relative;padding-left:25px;font-size:10.4px;line-height:13.8px;letter-spacing:-.05px}
  .hex-icon{position:absolute;left:0;top:1px;width:11px;height:12px}
  .risk-list{left:33px;top:398px;width:480px}
  .risk-list li{margin-bottom:8px}
  .track-list{left:182px;top:576px;width:384px}
  .track-list li{margin-bottom:7px;text-align:justify}
  .brand-name{font-family:"Fira Sans",sans-serif;font-weight:700;color:var(--navy)}
  .brand-lockup{left:398px;top:410px;display:flex;align-items:center;gap:10px;font-size:44px;line-height:50px}
  .brand-mark{width:44px;height:44px;border-radius:50%;background:var(--blue)}
  .brand-vertical{left:567px;top:88px;width:150px;display:flex;align-items:center;gap:10px;transform:rotate(-90deg);
    font-size:34px;line-height:40px}
  .brand-vertical .brand-name{color:var(--white)}
  .brand-vertical .brand-mark{width:40px;height:40px;background:var(--white);opacity:.9}
  .right-column{left:634px;top:309px;width:532px}
  .right-column .section-title{margin-top:14px;margin-bottom:9px}
  .right-column .body-copy + .body-copy{margin-top:9px}
  .doc-copy{width:313px}
  .tagline{left:700px;top:806px;width:420px;text-align:center;font-family:"Fira Sans",sans-serif;font-weight:700;
    font-size:23px;line-height:30px;color:var(--white);letter-spacing:.3px}
</style>
</head>
<body>
<main class="brochure">
  <svg class="shapes" viewBox="0 0 1200 849" xmlns="http://www.w3.org/2000/svg">
    <defs>
      <linearGradient id="bandBlue" x1="0" y1="0" x2="0" y2="1">
        <stop offset="0" stop-color="#3a4cb4"/>
        <stop offset="1" stop-color="#232870"/>
      </linearGradient>
      <linearGradient id="footBlue" x1="0" y1="0" x2="1" y2="0">
        <stop offset="0" stop-color="#2d3a9e"/>
        <stop offset="1" stop-color="#232870"/>
      </linearGradient>
      <linearGradient id="photoMeeting" x1="0" y1="0" x2="1" y2="1">
        <stop offset="0" stop-color="#c9d6e2"/>
        <stop offset=".5" stop-color="#5e7a98"/>
        <stop offset="1" stop-color="#a7b6c6"/>
      </linearGradient>
      <linearGradient id="photoTeam" x1="0" y1="0" x2="1" y2="1">
        <stop offset="0" stop-color="#7fb3cf"/>
        <stop offset=".5" stop-color="#e9eef3"/>
        <stop offset="1" stop-color="#8fa8c4"/>
      </linearGradient>
      <linearGradient id="photoWorker" x1="0" y1="0" x2="1" y2="1">
        <stop offset="0" stop-color="#c2ccd6"/>
        <stop offset=".6" stop-color="#4f8fc6"/>
        <stop offset="1" stop-color="#4b5563"/>
      </linearGradient>
      <linearGradient id="photoDesk" x1="0" y1="0" x2="0" y2="1">
        <stop offset="0" stop-color="#b9a39a"/>
        <stop offset=".55" stop-color="#e6e8ee"/>
        <stop offset="1" stop-color="#c9cbd2"/>
      </linearGradient>
    </defs>

    <rect x="0" y="0" width="600" height="849" fill="var(--paper-tint)"/>
    <rect x="0" y="157" width="320" height="150" fill="var(--band-grey)"/>

    <polygon points="448,0 700,0 700,204 580,303 448,150" fill="url(#bandBlue)"/>

    <g role="img" aria-label="Photo: dentist and practice manager talking in a bright dental clinic">
      <polygon points="448,81 580,157 580,309 448,384 314,309 314,157" fill="url(#photoMeeting)" stroke="#ffffff" stroke-width="6" stroke-linejoin="round"/>
    </g>

    <g role="img" aria-label="Photo: dentist and hygienist reviewing a compliance checklist on a tablet in an operatory">
      <polygon points="700,18 732,0 1200,0 1200,141 842,293 700,204" fill="url(#photoTeam)"/>
    </g>
    <polygon points="1200,141 1200,262 1060,208" fill="var(--blue)"/>
    <polygon points="975,246 1103,222 1200,270 1200,282 1012,270" fill="var(--navy)"/>

    <g role="img" aria-label="Photo: dental assistant checking sterilization records on a clipboard">
      <polygon points="0,518 145,600 145,772 20,849 0,849" fill="url(#photoWorker)"/>
    </g>
    <polygon points="145,600 152,604 152,768 145,772" fill="var(--blue)"/>

    <g role="img" aria-label="Photo: dental front desk with monitors showing compliance dashboards">
      <polygon points="1075,552 1185,612 1185,737 1075,795 968,737 968,612" fill="url(#photoDesk)" stroke="#ffffff" stroke-width="5" stroke-linejoin="round"/>
    </g>
    <polygon points="1185,612 1190,615 1190,740 1185,737" fill="var(--blue)"/>

    <polygon points="606,849 710,795 1082,795 1185,737 1200,737 1200,849" fill="url(#footBlue)"/>

    <g fill="#ffffff">
      <circle cx="516" cy="9" r="2.7"/><circle cx="530" cy="9" r="2.7"/><circle cx="543" cy="9" r="2.7"/><circle cx="557" cy="9" r="2.7"/><circle cx="571" cy="9" r="2.7"/>
      <circle cx="516" cy="23" r="2.7"/><circle cx="530" cy="23" r="2.7"/><circle cx="543" cy="23" r="2.7"/><circle cx="557" cy="23" r="2.7"/><circle cx="571" cy="23" r="2.7"/>
    </g>
    <g fill="var(--blue)">
      <circle cx="249" cy="158" r="2.8"/><circle cx="262" cy="158" r="2.8"/><circle cx="276" cy="158" r="2.8"/><circle cx="290" cy="158" r="2.8"/><circle cx="303" cy="158" r="2.8"/>
      <circle cx="1127" cy="248" r="2.8"/><circle cx="1139" cy="254" r="2.8"/><circle cx="1151" cy="261" r="2.8"/><circle cx="1163" cy="267" r="2.8"/><circle cx="1175" cy="273" r="2.8"/>
    </g>

    <g fill="none" stroke="#ffffff" stroke-width="2" stroke-linejoin="round">
      <path d="M1147,196 L1136,203 L1147,210"/><path d="M1157,196 L1146,203 L1157,210"/>
      <path d="M1178,194 L1166,203 L1178,212 Z" fill="#ffffff"/>
    </g>

    <g stroke="var(--blue)" stroke-width="1.6" stroke-linejoin="round">
      <path d="M693,247 L706,247 L699.5,256 Z" fill="var(--blue)"/>
      <path d="M693,255 L706,255 L699.5,264 Z" fill="none"/>
      <path d="M693,263 L706,263 L699.5,272 Z" fill="none"/>

      <path d="M549,507 L562,507 L555.5,498 Z" fill="none"/>
      <path d="M549,515 L562,515 L555.5,506 Z" fill="none"/>
      <path d="M549,523 L562,523 L555.5,514 Z" fill="var(--blue)"/>

      <path d="M131,812 L144,812 L137.5,821 Z" fill="var(--blue)"/>
      <path d="M131,820 L144,820 L137.5,829 Z" fill="none"/>
      <path d="M131,828 L144,828 L137.5,837 Z" fill="none"/>

      <path d="M1167,789 L1180,789 L1173.5,780 Z" fill="none"/>
      <path d="M1167,797 L1180,797 L1173.5,788 Z" fill="none"/>
      <path d="M1167,805 L1180,805 L1173.5,796 Z" fill="var(--blue)"/>
    </g>
  </svg>

  <p class="abs body-copy justify" style="left:34px;top:30px;width:396px;">Our compliance management platform is built on the most secure cloud-based network using the latest cutting edge software technologies. This comprehensive and affordable Compliance Management System is designed around the needs of dental practices and configured by our experienced team of Healthcare Compliance and Software Development Professionals.</p>

  <h1 class="abs heading main-title">Features and<br>Benefits</h1>

  <div class="abs brand-vertical"><span class="brand-mark"></span><span class="brand-name">Verixa</span></div>

  <h2 class="abs heading section-title" style="left:33px;top:336px;width:300px;">Reduce Risk and Liability with Efficiency &amp; Visibility</h2>

  <ul class="abs feature-list risk-list">
    <li><svg class="hex-icon" viewBox="0 0 11 12"><polygon points="5.5,1 10,3.5 10,8.5 5.5,11 1,8.5 1,3.5" fill="none" stroke="var(--navy)" stroke-width="2.2"/></svg>Customize office audits and inspections.</li>
    <li><svg class="hex-icon" viewBox="0 0 11 12"><polygon points="5.5,1 10,3.5 10,8.5 5.5,11 1,8.5 1,3.5" fill="none" stroke="var(--navy)" stroke-width="2.2"/></svg>Monitor and analyze performance across your practice.</li>
    <li><svg class="hex-icon" viewBox="0 0 11 12"><polygon points="5.5,1 10,3.5 10,8.5 5.5,11 1,8.5 1,3.5" fill="none" stroke="var(--navy)" stroke-width="2.2"/></svg>Reduce compliance related financial impact and liability.</li>
    <li><svg class="hex-icon" viewBox="0 0 11 12"><polygon points="5.5,1 10,3.5 10,8.5 5.5,11 1,8.5 1,3.5" fill="none" stroke="var(--navy)" stroke-width="2.2"/></svg>Increase accountability through assignment of responsibility.</li>
    <li><svg class="hex-icon" viewBox="0 0 11 12"><polygon points="5.5,1 10,3.5 10,8.5 5.5,11 1,8.5 1,3.5" fill="none" stroke="var(--navy)" stroke-width="2.2"/></svg>Verify staff participation in your training, audit, and inspection programs.</li>
    <li><svg class="hex-icon" viewBox="0 0 11 12"><polygon points="5.5,1 10,3.5 10,8.5 5.5,11 1,8.5 1,3.5" fill="none" stroke="var(--navy)" stroke-width="2.2"/></svg>Manage infection control, privacy and safety risks in one location.</li>
  </ul>

  <div class="abs brand-lockup"><span class="brand-mark"></span><span class="brand-name">Verixa</span></div>

  <h2 class="abs heading section-title" style="left:182px;top:540px;">Track Compliance and Performance</h2>

  <ul class="abs feature-list track-list">
    <li><svg class="hex-icon" viewBox="0 0 11 12"><polygon points="5.5,1 10,3.5 10,8.5 5.5,11 1,8.5 1,3.5" fill="none" stroke="var(--navy)" stroke-width="2.2"/></svg>Increase productivity through streamlined data collection, automated workflows, and faster reporting.</li>
    <li><svg class="hex-icon" viewBox="0 0 11 12"><polygon points="5.5,1 10,3.5 10,8.5 5.5,11 1,8.5 1,3.5" fill="none" stroke="var(--navy)" stroke-width="2.2"/></svg>Demonstrate your compliance efforts to inspectors and patients by capturing important data.</li>
    <li><svg class="hex-icon" viewBox="0 0 11 12"><polygon points="5.5,1 10,3.5 10,8.5 5.5,11 1,8.5 1,3.5" fill="none" stroke="var(--navy)" stroke-width="2.2"/></svg>Reduce incidents by shrinking the time from problem detection to remediation.</li>
    <li><svg class="hex-icon" viewBox="0 0 11 12"><polygon points="5.5,1 10,3.5 10,8.5 5.5,11 1,8.5 1,3.5" fill="none" stroke="var(--navy)" stroke-width="2.2"/></svg>Foster a culture of compliance by enabling your whole team to engage in your program.</li>
  </ul>

  <h2 class="abs heading section-title" style="left:182px;top:725px;">Audits &amp; Inspections</h2>
  <p class="abs body-copy justify" style="left:182px;top:757px;width:381px;">The Audit &amp; Inspection feature allows you to conduct infection control audits, sterilization checks, and operatory inspections across your practice using a single centralized software system. Options for pre-built or custom dental checklists are available to identify and assign non-conformances and</p>

  <section class="abs right-column">
    <p class="body-copy justify">potential hazards and instantly initiate corrective actions to bring your compliance up to speed. The system allows your practice to meet regulatory requirements as well as policy and accreditation standards. The Verixa platform can generate reports to identify trends and reveal areas of continuous improvement.</p>

    <h2 class="heading section-title">Training Management</h2>
    <p class="body-copy justify">The Training Management solution provides the tools needed to schedule trainings, document and verify completions, and deliver tailored content based on each team member's role, from dentists and hygienists to front desk staff. Built-in email notifications remind staff and office managers when training deadlines and license or certification dates are upcoming or past due.</p>
    <p class="body-copy justify">The software streamlines staff training and evaluation and allows you to easily administer training programs across your entire practice to help create a culture of continuous learning.</p>

    <h2 class="heading section-title">Document Management</h2>
    <p class="body-copy justify doc-copy">Verixa is a secure, customizable, and searchable repository for policies, procedures, exposure control plans, audits, and other practice documents. Your team will have immediate access to all required documents in one location.</p>
    <p class="body-copy justify doc-copy">Safety Data Sheets ensure team members handling disinfectants and other chemicals have the information they need to use them safely. The Safety Data Sheet (SDS) feature gives your practice instant access to its chemical inventory, ensuring safer handling in every operatory.</p>
  </section>

  <p class="abs tagline">Simplify. Centralize. Automate</p>
</main>
</body>
</html>
```